Corporate Reception Invite (Thursday Gather: CorkPop Series)

I am looking for an invitation to use in Constant Contact for an upcoming reception. I have attached the company logo and a hero image from the reception location that may work well. Lastly, I attached an example from last year's invite for reference. Event details:

Thursday Gather: CorkPop Series @ QRB
October 23rd, 2023 from 6:00 - 8:00 pm
Marcella at The Halvorsen, Chicago
418 N Pellham Ave, Chicago, IL 60699
Join RBK & Friends for Cocktails & Conversation
Super casual - come and go as you please. Guests welcome.

Target Market(s)

Corporate audience

Font styles to use
Serif
Script
Other font styles liked:
• No strong preference, but want something elegant, sexy, and corporate

Colors
0054AA
0677BA
7BADD7
CADEEF
E8F1F8

Requirements
Must have
• RBK logo, event details, size: 600 x 1500 pixels

```html
<!DOCTYPE html>
<html lang="en">
<head>
<meta charset="utf-8">
<title>Thursday Gather: CorkPop Series — Invitation</title>
<link href="https://fonts.googleapis.com/css2?family=Playfair+Display:wght@600;700;800&family=Great+Vibes&family=Poppins:wght@400;500;600;700&family=Oswald:wght@200;300;500;600&display=swap" rel="stylesheet">
<style>
  :root {
    --page: #dcdcdc;
    --navy: #0b1128;
    --sky: #7badd7;
    --bright: #5bbfea;
    --band: #0054aa;
    --white: #ffffff;
    --mist: #e8f1f8;
  }
  * { box-sizing: border-box; margin: 0; padding: 0; }
  html, body {
    width: 931px; height: 1200px; overflow: hidden;
    background: var(--page);
    font-family: "Poppins", sans-serif;
  }
  .invite {
    position: absolute; left: 237px; top: 30px;
    width: 456px; height: 1140px;
    background: var(--navy);
    overflow: hidden;
    box-shadow: 0 4px 10px rgba(0,0,0,.25);
    color: var(--white);
  }
  .hero-photo { position: absolute; left: 0; top: 0; width: 456px; height: 460px; }
  .dress-note {
    position: absolute; right: 24px; top: 296px; text-align: right;
    font-weight: 700; font-size: 12px; line-height: 15px;
  }
  .dress-note .welcome {
    display: block; font-weight: 400; font-size: 19px; line-height: 24px; color: var(--bright);
  }
  .title {
    position: absolute; left: 24px; top: 484px;
    font-family: "Playfair Display", serif;
    font-weight: 800; font-size: 54px; line-height: 58px; letter-spacing: 0.5px;
  }
  .subtitle {
    position: absolute; left: 26px; top: 610px;
    font-family: "Great Vibes", cursive;
    font-size: 40px; line-height: 48px; color: var(--bright);
  }
  .date-mark {
    position: absolute; left: 24px; top: 700px; width: 110px; height: 110px;
    background: var(--bright);
  }
  .date-day {
    position: absolute; left: 24px; top: 700px; width: 110px;
    font-family: "Oswald", sans-serif; font-weight: 600; font-size: 78px; line-height: 110px;
    color: var(--navy); text-align: center; letter-spacing: -2px;
  }
  .date-suffix {
    position: absolute; left: 142px; top: 706px;
    font-size: 12px; font-weight: 600;
  }
  .date-month {
    position: absolute; left: 168px; top: 698px;
    font-family: "Playfair Display", serif;
    font-weight: 700; font-size: 44px; line-height: 54px;
  }
  .date-year {
    position: absolute; left: 170px; top: 760px;
    font-family: "Oswald", sans-serif; font-weight: 200; font-size: 26px; letter-spacing: 2px; line-height: 30px;
  }
  .date-time {
    position: absolute; left: 244px; top: 764px; width: 188px; height: 24px;
    background: var(--band);
    font-size: 13px; line-height: 24px; text-align: center; font-weight: 400;
  }
  .date-time strong { font-weight: 600; }
  .venue {
    position: absolute; left: 24px; top: 840px;
    font-weight: 600; font-size: 16px; letter-spacing: 0.2px;
  }
  .address {
    position: absolute; left: 24px; top: 866px;
    font-size: 13px; font-weight: 400; display: flex; align-items: center; gap: 5px;
  }
  .address svg { width: 11px; height: 14px; }
  .host { position: absolute; left: 24px; top: 906px; display: flex; align-items: center; gap: 16px; }
  .host-brand { display: flex; align-items: center; gap: 8px; font-weight: 700; font-size: 24px; }
  .host-brand .dot { width: 20px; height: 20px; border-radius: 50%; background: var(--white); }
  .host-invite {
    font-family: "Oswald", sans-serif; font-weight: 500; font-size: 28px; color: var(--bright);
  }
  .host-invite .amp { font-weight: 300; color: var(--white); }
  .host-purpose {
    position: absolute; left: 24px; top: 952px;
    font-weight: 600; font-size: 12px; letter-spacing: 0.5px;
  }
  .rsvp { position: absolute; left: 24px; top: 990px; display: flex; flex-direction: column; gap: 10px; }
  .rsvp-button {
    width: 408px; height: 36px; border-radius: 9px;
    border: 1px solid var(--bright); color: var(--white);
    font-size: 13px; font-weight: 500; text-align: center; line-height: 34px;
  }
  .rsvp-button.is-primary { background: var(--bright); color: var(--navy); }
</style>
</head>
<body>
  <section class="invite">
    <svg class="hero-photo" viewBox="0 0 456 460" role="img" aria-label="Photo of red wine being poured into a row of wine glasses">
      <defs>
        <linearGradient id="wineTones" x1="0" y1="0" x2="1" y2="1">
          <stop offset="0" stop-color="#2f3e3c"/>
          <stop offset="0.45" stop-color="#5a3a3e"/>
          <stop offset="0.75" stop-color="#3a2a30"/>
          <stop offset="1" stop-color="#1a2224"/>
        </linearGradient>
      </defs>
      <polygon points="0,0 456,0 456,380 0,460" fill="url(#wineTones)"/>
    </svg>

    <p class="dress-note">SUPER CASUAL<br>COME &amp; GO AS YOU PLEASE<span class="welcome">GUESTS WELCOME</span></p>

    <h1 class="title">THURSDAY<br>GATHER</h1>
    <p class="subtitle">CorkPop Series @ QRB</p>

    <div class="date-mark" role="img" aria-label="Decorative date ornament"></div>
    <span class="date-day">23</span>
    <span class="date-suffix">RD</span>
    <span class="date-month">OCTOBER</span>
    <span class="date-year">2023</span>
    <span class="date-time">FROM | <strong>6:00 – 8:00 PM</strong></span>

    <p class="venue">MARCELLA AT THE HALVORSEN, CHICAGO</p>
    <p class="address">
      <svg viewBox="0 0 11 14" aria-hidden="true"><path d="M5.5 0A5.5 5.5 0 0 0 0 5.5C0 9.5 5.5 14 5.5 14S11 9.5 11 5.5A5.5 5.5 0 0 0 5.5 0Zm0 7.6a2.1 2.1 0 1 1 0-4.2 2.1 2.1 0 0 1 0 4.2Z" fill="var(--bright)"/></svg>
      418 N Pellham Ave, Chicago, IL 60699
    </p>

    <div class="host">
      <span class="host-brand"><span class="dot"></span>RBK</span>
      <span class="host-invite">JOIN RBK <span class="amp">&amp;</span> FRIENDS</span>
    </div>
    <p class="host-purpose">FOR COCKTAILS &amp; CONVERSATION</p>

    <div class="rsvp">
      <span class="rsvp-button is-primary">Cheers! I’ll be there</span>
      <span class="rsvp-button">I’ll try to stop by</span>
      <span class="rsvp-button">Sorry, I can’t make it</span>
    </div>
  </section>
</body>
</html>
```